Business Card Design

I need a business card design for my new business based on Long Island, NY also serving NYC called Pine Hollow Kennel. I have built a website with printwell that can be looked at as a basis for the card. It is pinehollowkennel.example.

I board Labrador Retrievers in my home. Specialize in one breed. Cage free environment. Dogs have full run of home and fenced in property. Pine Hollow Kennel is a one-of-a-kind, high-quality dog-boarding provider serving specifically Labrador Retrievers. By working with a dog I am comfortable with, I am able to offer the best care for all pets that come through my door. I work with Lab owners in the Long Island/NYC area to provide an
in-home safe, reliable and fun environment for daycare and overnight stays.

I provide a unique boarding experience for Labrador Retrievers on Long Island. Your Lab should be well mannered, housebroken and good with other dogs. Provided your pet is well mannered and house trained, my boarding services allow dogs to experience a cage-free stay while having free roam of my home and property. This allows owners a unique alternative to a kennel, giving pets the chance to experience a home away from home rather than chain linked fences and cold concrete floors.
As a guest at Pine Hollow Kennel, your dog will get:

4-star kibble
Access to my in-ground pool
All-natural snack selection
Companionship of other retrievers including my two
Full run of entire home and fenced-in backyard
Photos AND videos posted to Chatterpage so you can see your dog having fun while away
Toys, bones and affection

I think it is important to have a pic of the 3 colored labs below. Also the picture of my own personal labs ..the white one with the black puppy. Maybe some paw prints. If using any imagery that MUST look EXACTLY like labrador retriever no generic dogs. Thank you
Updates

The Back of the Card should have the following: The background should be one of the pictures I sent (white dog in pool or another pic I included) At Pine Hollow Kennel your Lab gets: Cage Free Environment Full run of my home and fenced in yard In-ground pool Toys and affection Companionship of other Labrador Retrievers Photos and Videos posted Chatterpage of your loved one FRONT OF THE CARD: should include picture of the 3 labs (yellow white brown) OR picture of white dog in pool. Pine Hollow Kennel should be in larger font than the rest. the following can be in any order. Rick Dunmore Commack, NY in Central Long Island pinehollowkennel.example 631-555-0194

Industry/Entity Type

Environment

Contact Information for Business Card

Pine Hollow Kennel
Commack, NY
Rick Dunmore
pinehollowkennel@mailbox.example
631-555-0194

```html
<!DOCTYPE html>
<html lang="en">
<head>
<meta charset="utf-8">
<title>Pine Hollow Kennel – Business Card</title>
<link rel="stylesheet" href="https://fonts.googleapis.com/css2?family=Marcellus+SC&family=Arimo:wght@400&display=swap">
<style>
  :root {
    --page-bg: #e6e4e1;
    --card-dark: #333333;
    --card-dark-light: #4b4b4b;
    --card-white: #ffffff;
    --band-brown: #6b5750;
    --band-white: #f4f2ef;
    --photo-grass: #7d9a52;
    --photo-cream: #e8dcc0;
    --photo-brown: #3a2a22;
    --text-light: #f2f2f2;
    --text-dark: #1c1c1c;
    --star: #555555;
  }
  * { margin: 0; padding: 0; box-sizing: border-box; }
  html, body {
    width: 1200px;
    height: 914px;
    overflow: hidden;
    background: var(--page-bg);
  }
  .canvas {
    position: relative;
    width: 1200px;
    height: 914px;
  }
  .card {
    position: absolute;
    left: 250px;
    width: 700px;
    height: 400px;
    overflow: hidden;
    box-shadow: 0 6px 18px rgba(0,0,0,0.18);
  }
  /* Back of card */
  .card-back {
    top: 38px;
    background: var(--card-white);
    color: var(--text-dark);
    font-family: "Arimo", Arial, sans-serif;
    padding: 62px 30px 0 90px;
  }
  .back-heading {
    font-size: 23px;
    font-weight: 400;
    white-space: nowrap;
    margin-bottom: 14px;
  }
  .perks {
    list-style: none;
    font-size: 17px;
    line-height: 1.3;
    padding-left: 24px;
    max-width: 520px;
  }
  .perks li {
    position: relative;
    padding-left: 24px;
  }
  .perks li::before {
    content: "\2736";
    position: absolute;
    left: 0;
    top: 0;
    font-size: 13px;
    color: var(--star);
  }
  /* Front of card */
  .card-front {
    top: 476px;
    background: radial-gradient(ellipse at 35% 90%, var(--card-dark-light) 0%, var(--card-dark) 70%);
    color: var(--text-light);
  }
  .front-art {
    position: absolute;
    inset: 0;
    width: 700px;
    height: 400px;
  }
  .business-name {
    position: absolute;
    top: 58px;
    right: 28px;
    font-family: "Marcellus SC", Georgia, serif;
    font-size: 24px;
    line-height: 1.3;
    letter-spacing: 1px;
    font-weight: 400;
    text-align: right;
  }
  .business-name span { display: block; white-space: nowrap; }
  .owner {
    position: absolute;
    top: 150px;
    right: 30px;
    font-family: "Arimo", Arial, sans-serif;
    font-size: 22px;
  }
  .contact {
    position: absolute;
    right: 30px;
    bottom: 52px;
    font-family: "Arimo", Arial, sans-serif;
    font-size: 16px;
    list-style: none;
    text-align: right;
    line-height: 1.45;
  }
  .contact li {
    display: flex;
    justify-content: flex-end;
    align-items: center;
    gap: 12px;
    white-space: nowrap;
  }
  .contact svg { width: 15px; height: 15px; fill: var(--text-light); }
</style>
</head>
<body>
<main class="canvas">

  <section class="card card-back">
    <h2 class="back-heading">As a guest at Pine Hollow Kennel, your dog will get</h2>
    <ul class="perks">
      <li>4-star kibble</li>
      <li>Access to my in-ground pool</li>
      <li>All-natural snack selection</li>
      <li>Companionship of other retrievers including my two</li>
      <li>Full run of entire home and fenced-in backyard</li>
      <li>Photos AND videos posted to Chatterpage so you can see your dog having fun while away</li>
      <li>Toys, bones and affection</li>
    </ul>
  </section>

  <section class="card card-front">
    <svg class="front-art" viewBox="0 0 700 400">
      <defs>
        <linearGradient id="photoTones" x1="0" y1="0" x2="1" y2="1">
          <stop offset="0" stop-color="var(--photo-grass)"/>
          <stop offset="0.3" stop-color="var(--photo-brown)"/>
          <stop offset="0.55" stop-color="var(--photo-cream)"/>
          <stop offset="0.8" stop-color="var(--photo-brown)"/>
          <stop offset="1" stop-color="var(--photo-grass)"/>
        </linearGradient>
      </defs>
      <path class="band-brown" d="M0 0 H352 Q452 200 318 400 H0 Z" fill="var(--band-brown)"/>
      <path class="band-white" d="M0 0 H338 Q436 200 305 400 H0 Z" fill="var(--band-white)"/>
      <path class="dog-photo" role="img" aria-label="Photo of three Labrador retrievers – chocolate, yellow and black – sitting on grass" d="M0 0 H332 Q428 200 298 400 H0 Z" fill="url(#photoTones)"/>
    </svg>

    <h1 class="business-name"><span>Pine Hollow Kennel</span><span>Commack</span></h1>
    <p class="owner">NY Rick Dunmore</p>
    <ul class="contact">
      <li>631-555-0194
        <svg viewBox="0 0 16 16" aria-label="phone"><path d="M4 1 L6.5 4 L5 6 Q6.5 9.5 10 11 L12 9.5 L15 12 L13 15 Q5 14 1 3 Z"/></svg>
      </li>
      <li>pinehollowkennel@mailbox.example
        <svg viewBox="0 0 16 16" aria-label="email"><path d="M1 3 H15 V13 H1 Z M2 4 L8 9 L14 4 Z" fill-rule="evenodd"/></svg>
      </li>
    </ul>
  </section>

</main>
</body>
</html>
```